existing Business Card Re design

We are wanting to re design our cards to reflect our new logo , i have attache the current business cards and new logo
i will need a business card that reflects the following information on each card.

card 1:
Gordon Thibeaux, President
555-182-4407
info@qlmcoatingpro.example

card 2:
Lionel Ostrander, Outside Sales
Office: 555-182-4407
Cell: 555-631-2958
Sales@qlmcoatingpro.example

Card 3
Tomas Varley, Branch Manager
Office: 555-182-4407
Cell: 555-274-8163
Tomas@qlmcoatingpro.example

Card 4
I will need a Generic card with no name on it just business
555-182-4407
info@qlmcoatingpro.example

Target Market(s)

Homeowners and Contractors

Contact Information for Business Card

We are wanting to re design our cards to reflect our new logo , i have attache the current business cards and new logo. same info on current card

card 1:
Gordon Thibeaux, President
555-182-4407
info@qlmcoatingpro.example

card 2:
Office: 555-182-4407
Cell: 555-631-2958
Sales@qlmcoatingpro.example

Card 3
Office: 555-182-4407
Cell: 555-274-8163
Tomas@qlmcoatingpro.example

Card 4
555-182-4407
info@qlmcoatingpro.example

Requirements
Must have
• same info as current cards with a added business
"sanitizing"

```html
<!DOCTYPE html>
<html lang="en">
<head>
<meta charset="UTF-8">
<title>QLM Coating Pro – Business Card</title>
<link rel="stylesheet" href="https://fonts.googleapis.com/css2?family=Oswald:wght@500&family=Montserrat:wght@400;700&display=swap">
<style>
  :root {
    --backdrop: #0d0d0d;
    --card: #1f1f1f;
    --card-edge: #2a2a2a;
    --silver: #a9a9a9;
    --silver-soft: #8e8e8e;
    --divider: #6f6f6f;
  }
  * { box-sizing: border-box; margin: 0; padding: 0; }
  html, body {
    width: 1200px;
    height: 900px;
    overflow: hidden;
    background: var(--backdrop);
  }
  .stage {
    width: 1200px;
    height: 900px;
    display: flex;
    flex-direction: column;
    align-items: center;
    justify-content: center;
    gap: 46px;
  }
  .card {
    width: 600px;
    height: 343px;
    background: var(--card);
    border: 1px solid var(--card-edge);
    position: relative;
  }
  .card-front {
    display: flex;
    align-items: center;
    justify-content: center;
    gap: 16px;
  }
  .brand-mark {
    width: 26px;
    height: 26px;
    background: var(--silver);
  }
  .brand-name {
    font-family: "Montserrat", sans-serif;
    font-weight: 700;
    font-size: 38px;
    letter-spacing: -0.5px;
    color: var(--silver);
  }
  .card-back {
    display: flex;
    align-items: center;
    justify-content: center;
    padding-top: 10px;
  }
  .identity {
    text-align: right;
    padding-right: 26px;
  }
  .person-name {
    font-family: "Oswald", sans-serif;
    font-weight: 500;
    font-size: 30px;
    letter-spacing: 1px;
    text-transform: uppercase;
    color: var(--silver);
    line-height: 1.1;
  }
  .person-role {
    font-family: "Montserrat", sans-serif;
    font-weight: 400;
    font-size: 14px;
    color: var(--silver-soft);
    margin-top: 4px;
  }
  .divider {
    width: 1px;
    height: 62px;
    background: var(--divider);
  }
  .contact-list {
    list-style: none;
    padding-left: 26px;
    padding-top: 22px;
  }
  .contact-item {
    display: flex;
    align-items: center;
    gap: 8px;
    font-family: "Montserrat", sans-serif;
    font-size: 14px;
    color: var(--silver);
    line-height: 21px;
  }
  .contact-icon {
    width: 10px;
    height: 10px;
    fill: none;
    stroke: var(--silver);
    stroke-width: 1.4;
  }
</style>
</head>
<body>
<main class="stage">
  <section class="card card-front" aria-label="Card front">
    <span class="brand-mark"></span>
    <span class="brand-name">QLM Coating Pro</span>
  </section>

  <section class="card card-back" aria-label="Card back">
    <div class="identity">
      <p class="person-name">Lionel Ostrander</p>
      <p class="person-role">Outside Sales</p>
    </div>
    <span class="divider"></span>
    <ul class="contact-list">
      <li class="contact-item">
        <svg class="contact-icon" viewBox="0 0 10 10" aria-hidden="true"><path d="M2 1 L3.5 1 L4.2 3 L3.2 3.8 Q4.2 5.8 6.2 6.8 L7 5.8 L9 6.5 L9 8 Q8.5 9 7.5 9 Q1 8 1 2 Q1 1 2 1 Z"/></svg>
        <span>555-182-4407</span>
      </li>
      <li class="contact-item">
        <svg class="contact-icon" viewBox="0 0 10 10" aria-hidden="true"><rect x="2.5" y="0.8" width="5" height="8.4" rx="0.8"/><line x1="4.3" y1="7.6" x2="5.7" y2="7.6"/></svg>
        <span>555-631-2958</span>
      </li>
      <li class="contact-item">
        <svg class="contact-icon" viewBox="0 0 10 10" aria-hidden="true"><rect x="0.8" y="2" width="8.4" height="6" rx="0.6"/><path d="M1 2.4 L5 5.4 L9 2.4"/></svg>
        <span>Sales@qlmcoatingpro.example</span>
      </li>
    </ul>
  </section>
</main>
</body>
</html>
```